Website Design for A Nook for Grandpas

Please design and code a new website.
Here are the sites I like best:
http://www.sailbeacon.net/alternate/
http://www.wheelsgiving.net
Please make it similar but look at the competitor site (below) for images and wording. This is NOT a car donation site. It's a senior lead placement site like https://www.eldernestfinder.net. I just like this sites above as a lead generation sites.
Competitor site:
https://www.eldernestfinder.net (use ideas / verbiage from this site)
Updates
Competitor site:

```html
<!DOCTYPE html>
<html lang="en">
<head>
<meta charset="utf-8">
<title>A Nook for Grandpas — Find Senior Living Near You</title>
<link href="https://fonts.googleapis.com/css2?family=Oswald:wght@400;500;600&family=Roboto:ital,wght@0,400;0,500;0,700;1,400&family=Roboto+Condensed:wght@700&display=swap" rel="stylesheet">
<style>
:root{
  --teal:#2db3a1;
  --teal-dark:#1f9a8c;
  --navy:#0b3c63;
  --navy-deep:#082f52;
  --blue:#155a86;
  --green:#6aa51c;
  --green-light:#86c02a;
  --ink:#2b2b2b;
  --grey:#8a8a8a;
  --line:#dcdcdc;
  --panel:#f3f3f3;
  --outer:#dfe7ee;
  --white:#ffffff;
}
*{box-sizing:border-box;margin:0;padding:0}
html,body{width:1200px;height:2860px;overflow:hidden}
body{background:var(--outer);font-family:"Roboto",sans-serif;color:var(--ink)}
.page{position:absolute;left:100px;top:0;width:1000px;height:2860px;background:var(--white);overflow:hidden}
.abs{position:absolute}
.center{text-align:center;left:0;width:1000px}

/* header */
.brand{left:120px;top:36px;display:flex;align-items:center;gap:10px;font-size:26px;font-weight:400;color:var(--navy)}
.brand-dot{width:16px;height:16px;border-radius:50%;background:var(--teal)}
.hotline{left:570px;top:0;width:309px;height:100px;background:linear-gradient(180deg,#3cc0ad,var(--teal-dark));color:var(--white)}
.hotline svg{position:absolute;left:24px;top:32px}
.hotline .t1{position:absolute;left:80px;top:45px;font-size:15px}
.hotline .t2{position:absolute;left:80px;top:65px;font-size:21px;font-weight:500}
.nav{left:0;top:100px;width:1000px;height:34px;background:linear-gradient(180deg,var(--blue),var(--navy-deep));display:flex;gap:31px;padding-left:133px;align-items:center}
.nav span{font-family:"Roboto Condensed",sans-serif;font-size:12px;color:var(--white);font-weight:700}

/* hero */
.hero{left:0;top:134px;width:1000px;height:516px;background:linear-gradient(120deg,#4d6a33 0%,#7e9454 35%,#c7a79b 55%,#8b9cb1 75%,#5f7153 100%);clip-path:polygon(0 0,100% 0,100% 432px,50% 516px,0 432px)}
.hero-title{left:118px;top:312px;font-family:"Oswald",sans-serif;font-weight:600;font-size:56px;line-height:58px;color:var(--white);text-transform:uppercase}
.field{background:var(--white);border:1px solid #d6d6d6;font-size:10px;color:#666;padding-left:15px;display:flex;align-items:center}
.btn{background:linear-gradient(180deg,var(--green-light),var(--green));color:var(--white);font-weight:700;font-size:13px;display:flex;align-items:center;justify-content:center}
.hero-arrow{width:40px;height:40px;border:1.5px solid var(--white);border-radius:50%;display:flex;align-items:center;justify-content:center}
.dots{left:477px;top:607px;display:flex;gap:3px}
.dots i{width:9px;height:9px;border-radius:50%;background:#cfcfcf;display:block}
.dots i:first-child{background:var(--teal)}

/* support */
.h2{font-family:"Oswald",sans-serif;font-weight:400;font-size:33px;color:var(--ink)}
.lead{font-size:11.5px;line-height:20px;color:var(--grey)}
.feature{width:150px;text-align:center}
.feature .ring{width:112px;height:112px;margin:0 auto;border:2px solid var(--teal);border-radius:50%;display:flex;align-items:center;justify-content:center}
.feature .ring div{width:98px;height:98px;border:3px solid var(--navy);border-radius:50%;display:flex;align-items:center;justify-content:center}
.feature p{margin-top:10px;font-family:"Oswald",sans-serif;font-size:14px;line-height:19px;color:#444;font-weight:400}

.quote-box{left:119px;top:1147px;width:762px;height:149px;background:var(--panel)}
.quote-photo{left:150px;top:1103px;width:220px;height:193px;background:linear-gradient(180deg,#e6e3df,#b9c4d0)}
.quote-text{left:417px;top:1167px;width:430px;font-size:12px;line-height:23px;font-style:italic;color:#888}
.quote-name{left:417px;top:1258px;font-size:12px;color:var(--teal);font-weight:500}
.quote-call{left:517px;top:1246px;display:flex;align-items:center;gap:8px;font-family:"Oswald",sans-serif;font-size:22px;color:var(--teal)}

/* advisor band */
.band{left:0;top:1382px;width:1000px;height:640px}
.band-title{top:1476px;font-family:"Oswald",sans-serif;font-size:32px;color:var(--white)}
.band-text{top:1545px;font-size:12.5px;line-height:23px;color:var(--white)}
.avatar{border-radius:50%;background:linear-gradient(160deg,#c9b9a5,#6d7e92);border:3px solid rgba(255,255,255,.25)}
.avatar-feature{border-radius:50%;background:rgba(53,184,164,.92);border:3px solid var(--white);color:var(--white);text-align:center;font-size:10px;line-height:18px;font-style:italic;font-weight:700;display:flex;flex-direction:column;justify-content:center}
.testi{width:200px;text-align:center;color:var(--white);font-size:9.5px;line-height:18px;font-style:italic}
.testi b{display:block;margin-top:5px;font-style:normal;font-size:9.5px}

/* states */
.tab{left:121px;width:191px;height:40px;border:1px solid var(--line);display:flex;align-items:center;justify-content:space-between;padding:0 14px 0 22px;font-size:12px;font-weight:500;color:#444}
.tab.on{background:var(--teal);color:var(--white);border-color:var(--teal)}
.tab i{width:9px;height:9px;border-radius:50%;background:#333;position:relative;display:block}
.tab.on i{background:var(--white)}
.tab i::after{content:"";position:absolute;left:2px;top:4px;width:5px;height:1px;background:var(--white)}
.tab.on i::after{background:var(--teal)}
.tab i.plus::before{content:"";position:absolute;left:4px;top:2px;width:1px;height:5px;background:var(--white)}
.states{left:358px;top:2181px;width:522px;height:232px;background:var(--white);box-shadow:0 2px 10px rgba(0,0,0,.13)}
.states ul{position:absolute;top:28px;list-style:none;font-size:11px;line-height:23.6px;color:#555}
.scroll{left:515px;top:89px;width:6px;height:50px;background:#e1e1e1}

/* footer */
.footer{left:0;top:2492px;width:1000px;height:368px}
.fh{top:2596px;font-size:14px;font-weight:500;color:#333}
.ft{font-size:9.8px;line-height:18px;color:#666}
.flist{list-style:none}
.flist li::before{content:"» ";color:var(--teal)}
.social{width:32px;height:32px;border-radius:50%;border:1.5px solid #333;background:var(--white)}
.sub{left:710px;top:2721px;width:86px;height:26px;border-radius:13px;background:var(--teal);color:var(--white);font-size:10.5px;font-weight:700;display:flex;align-items:center;justify-content:center}
</style>
</head>
<body>
<div class="page">

  <!-- header -->
  <div class="abs brand"><span class="brand-dot"></span>A Nook for Grandpas</div>
  <div class="abs hotline">
    <svg width="44" height="44" viewBox="0 0 44 44"><circle cx="22" cy="22" r="20" fill="none" stroke="#fff" stroke-width="2.5"/><path d="M15 12c2 0 3 4 3 5s-2 2-2 3c1 3 4 6 7 7 1 0 2-2 3-2s5 1 5 3-2 4-4 4c-8 0-16-8-16-16 0-2 2-4 4-4z" fill="#fff"/></svg>
    <div class="t1">Talk to a local advisor for FREE</div>
    <div class="t2">1 888 888 8888</div>
  </div>
  <nav class="abs nav">
    <span>ASSISTED LIVING</span><span>MEMORY CARE</span><span>NURSING HOMES</span><span>MORE LIVING OPTIONS</span><span>PLANNING &amp; ADVICE</span><span>HOW OUR SERVICE WORKS</span>
  </nav>

  <!-- hero -->
  <div class="abs hero" role="img" aria-label="Photo of a smiling young caregiver embracing a senior man outdoors"></div>
  <h1 class="abs hero-title">Find Senior<br>Living Near You</h1>
  <div class="abs field" style="left:120px;top:450px;width:263px;height:35px">Email Address</div>
  <div class="abs btn" style="left:120px;top:500px;width:136px;height:36px;border-radius:18px">Start Your Search</div>
  <div class="abs hero-arrow" style="left:43px;top:373px"><svg width="12" height="14"><path d="M9 1 3 7l6 6" fill="none" stroke="#fff" stroke-width="2"/></svg></div>
  <div class="abs hero-arrow" style="left:917px;top:373px"><svg width="12" height="14"><path d="M3 1l6 6-6 6" fill="none" stroke="#fff" stroke-width="2"/></svg></div>
  <div class="abs dots"><i></i><i></i><i></i><i></i></div>

  <!-- support -->
  <h2 class="abs center h2" style="top:728px">The support you need to make the RIGHT CHOICE</h2>
  <p class="abs center lead" style="top:790px">Sed ut perspiciatis unde omnis iste natus error sit voluptatem accusantium doloremque laudantium, totam rem aperiam,<br>eaque ipsa quae ab illo inventore veritatis et quasi architecto beatae vitae dicta sunt explicabo.</p>

  <div class="abs feature" style="left:101px;top:873px">
    <div class="ring"><div><svg width="50" height="46" viewBox="0 0 50 46" fill="none" stroke="#0b3c63" stroke-width="2"><rect x="4" y="4" width="16" height="14"/><text x="8" y="16" font-size="11" fill="#0b3c63" stroke="none">$</text><circle cx="32" cy="18" r="7"/><path d="M20 42c0-8 5-13 12-13s12 5 12 13"/></svg></div></div>
    <p>Dedicated local<br>advisor</p>
  </div>
  <div class="abs feature" style="left:263px;top:873px">
    <div class="ring"><div><svg width="52" height="46" viewBox="0 0 52 46" fill="none" stroke="#0b3c63" stroke-width="2"><path d="M16 18 26 8l10 10v10H16z"/><rect x="23" y="21" width="6" height="7"/><path d="M4 20v12l10 10h8M48 20v12L38 42h-8"/></svg></div></div>
    <p>Hand-picked list of<br>communities to<br>match your needs</p>
  </div>
  <div class="abs feature" style="left:425px;top:873px">
    <div class="ring"><div><svg width="46" height="48" viewBox="0 0 46 48" fill="none" stroke="#0b3c63" stroke-width="2"><circle cx="23" cy="20" r="14"/><text x="18" y="26" font-size="16" fill="#0b3c63" stroke="none">$</text><path d="M14 32 9 44l6-2 3 5 4-11M32 32l5 12-6-2-3 5-4-11"/></svg></div></div>
    <p>Full details and<br>pricing</p>
  </div>
  <div class="abs feature" style="left:586px;top:873px">
    <div class="ring"><div><svg width="50" height="44" viewBox="0 0 50 44" fill="none" stroke="#0b3c63" stroke-width="2"><rect x="4" y="6" width="42" height="34"/><path d="M4 14h42M14 2v8M36 2v8M14 20h22v12H14zM25 20v12M14 26h22"/></svg></div></div>
    <p>Help scheduling<br>tours</p>
  </div>
  <div class="abs feature" style="left:748px;top:873px">
    <div class="ring"><div><svg width="54" height="40" viewBox="0 0 54 40" fill="none" stroke="#0b3c63" stroke-width="2"><path d="M2 6h32v24H2zM34 14h10l8 8v8H34"/><circle cx="12" cy="32" r="4" fill="#fff"/><circle cx="42" cy="32" r="4" fill="#fff"/></svg></div></div>
    <p>Move in<br>support</p>
  </div>

  <!-- quote -->
  <div class="abs quote-box"></div>
  <div class="abs quote-photo" role="img" aria-label="Portrait photo of a senior man in a light blue polo shirt"></div>
  <p class="abs quote-text">Sed ut perspiciatis unde omnis iste natus error sit voluptatem accusantium dolor-emque laudantium, totam rem aperiam, eaque ipsa quae ab illo inventore veritatis et quasi architecto beatae vitae dicta sunt explicabo</p>
  <div class="abs quote-name">- JOHN DOE</div>
  <div class="abs quote-call"><svg width="38" height="38" viewBox="0 0 44 44"><circle cx="22" cy="22" r="20" fill="none" stroke="#0b3c63" stroke-width="2.5"/><path d="M15 12c2 0 3 4 3 5s-2 2-2 3c1 3 4 6 7 7 1 0 2-2 3-2s5 1 5 3-2 4-4 4c-8 0-16-8-16-16 0-2 2-4 4-4z" fill="#0b3c63"/></svg>Call 1 888 888 8888</div>

  <!-- advisor band -->
  <svg class="abs band" viewBox="0 0 1000 640" preserveAspectRatio="none" role="img" aria-label="Deep blue band over a faint photo of seniors">
    <defs><linearGradient id="bandFill" x1="0" y1="0" x2="0" y2="1"><stop offset="0" stop-color="#1a5f87"/><stop offset="1" stop-color="#07305a"/></linearGradient></defs>
    <polygon points="0,83 0,0 180,40" fill="#2db3a1"/>
    <polygon points="0,40 500,0 1000,76 1000,565 500,638 0,565" fill="url(#bandFill)"/>
    <polygon points="1000,486 1000,640 830,592" fill="#2db3a1"/>
  </svg>
  <h2 class="abs center band-title">Your LOCAL ADVISOR informs. You decide</h2>
  <p class="abs center band-text">Lorem ipsum dolor sit amet, consectetur adipiscing elit, sed do eiusmod tempor incididunt ut labore et dolore magna<br>Duis aute irure dolor in reprehenderit in voluptate velit esse cillum dolore eu fugiat nulla pariatur</p>
  <div class="abs field" style="left:286px;top:1618px;width:285px;height:35px">Enter City or postal code</div>
  <div class="abs btn" style="left:578px;top:1618px;width:137px;height:35px;border-radius:2px">Start Your Search</div>

  <div class="abs avatar" style="left:194px;top:1696px;width:124px;height:124px" role="img" aria-label="Photo of a smiling senior man with glasses"></div>
  <div class="abs testi" style="left:156px;top:1827px">" Lorem ipsum dolor sit amet, consecte-<br>tempor incididunloa aliqua "<b>JERRY H.</b></div>
  <div class="abs avatar-feature" style="left:410px;top:1693px;width:180px;height:180px">Lorem ipsum dolor sit amet,<br>consectetur adipiscing elit,<br>sed do eiusmod<br><span style="font-style:normal;margin-top:6px">JERRY H.</span></div>
  <div class="abs avatar" style="left:681px;top:1696px;width:124px;height:124px" role="img" aria-label="Photo of a senior man wearing sunglasses"></div>
  <div class="abs testi" style="left:643px;top:1827px">" Lorem ipsum dolor sit amet, consecte-<br>tempor incididunloa aliqua "<b>JERRY H.</b></div>
  <div class="abs btn" style="left:400px;top:1905px;width:200px;height:36px;border-radius:18px">SEE MORE TESTIMONIALS</div>

  <!-- states -->
  <h2 class="abs center h2" style="top:2095px">Senior Living by State</h2>
  <div class="abs tab on" style="top:2181px">Assisted Living<i></i></div>
  <div class="abs tab" style="top:2229px">Memory Care<i class="plus"></i></div>
  <div class="abs tab" style="top:2277px">Independent Living<i class="plus"></i></div>
  <div class="abs tab" style="top:2325px">Nursing Home<i class="plus"></i></div>
  <div class="abs tab" style="top:2373px">Care Homes<i class="plus"></i></div>
  <div class="abs states">
    <ul style="left:33px"><li>Alabama</li><li>Arizona</li><li>Arkansas</li><li>California</li><li>Colorado</li><li>Connecticut</li><li>Delaware</li><li>District of Columbia</li></ul>
    <ul style="left:185px"><li>Florida</li><li>Georgia</li><li>Hawaii</li><li>Idaho</li><li>Illinois</li><li>Indiana</li><li>Iowa</li><li>Kansas</li></ul>
    <ul style="left:285px"><li>Kentucky</li><li>Louisiana</li><li>Maine</li><li>Maryland</li><li>Massachusetts</li><li>Michigan</li><li>Minnesota</li><li>Mississippi</li></ul>
    <ul style="left:412px"><li>Missouri</li><li>Montana</li><li>Nebraska</li><li>Nevada</li><li>New Hampshire</li><li>New Jersey</li><li>New Mexico</li><li>New York</li></ul>
    <div class="abs scroll"></div>
  </div>

  <!-- footer -->
  <svg class="abs footer" viewBox="0 0 1000 368" preserveAspectRatio="none">
    <polygon points="0,20 500,0 1000,80 1000,368 0,368" fill="#f4f4f4"/>
    <polygon points="0,0 175,58 0,78" fill="#0b3c63"/>
    <circle cx="500" cy="10" r="26" fill="#fff"/>
    <path d="M500 22V0M492 8l8-8 8 8" fill="none" stroke="#222" stroke-width="2"/>
    <line x1="121" y1="291" x2="400" y2="291" stroke="#d4d4d4"/>
    <line x1="600" y1="291" x2="879" y2="291" stroke="#d4d4d4"/>
  </svg>
  <div class="abs fh" style="left:121px">ABOUT US</div>
  <div class="abs fh" style="left:352px">NAVIGATION</div>
  <div class="abs fh" style="left:497px">CONTACT INFO</div>
  <div class="abs fh" style="left:713px">SIGN UP NEWSLETTER</div>
  <p class="abs ft" style="left:121px;top:2628px;width:190px">Lorem ipsum dolor sit amet, consectetur adipiscing elit, sed do eiusmod tempor incididunt ut labore et dolore magna aliqua. Ut enim ad minim veniam</p>
  <ul class="abs ft flist" style="left:352px;top:2630px;line-height:21px"><li>Become a partner</li><li>See employment</li><li>opportunities</li><li>Contact us</li></ul>
  <div class="abs" style="left:497px;top:2638px"><svg width="28" height="28"><circle cx="14" cy="14" r="13" fill="#fff" stroke="#ccc"/><path d="M14 7a5 5 0 0 0-5 5c0 4 5 9 5 9s5-5 5-9a5 5 0 0 0-5-5z" fill="#0b3c63"/><circle cx="14" cy="12" r="1.8" fill="#fff"/></svg></div>
  <p class="abs ft" style="left:536px;top:2634px">234,Lorem ipsum dolor sit<br>amet, consectetur</p>
  <div class="abs" style="left:497px;top:2685px"><svg width="28" height="28"><circle cx="14" cy="14" r="13" fill="#fff" stroke="#ccc"/><path d="M10 8c1 0 2 3 2 3l-1 2c1 2 2 3 4 4l2-1s3 1 3 2-1 2-2 2c-5 0-10-5-10-10 0-1 1-2 2-2z" fill="#0b3c63"/></svg></div>
  <p class="abs ft" style="left:536px;top:2691px">Phone : 1 888 888 8888</p>
  <p class="abs ft" style="left:712px;top:2634px;line-height:16px">Register your Email Address to get<br>Information about us</p>
  <div class="abs field" style="left:713px;top:2677px;width:167px;height:30px;font-size:9.5px;padding-left:10px">Email Address</div>
  <div class="abs sub">SUBSCRIBE</div>
  <div class="abs social" style="left:421px;top:2767px"></div>
  <div class="abs social" style="left:463px;top:2767px"></div>
  <div class="abs social" style="left:505px;top:2767px"></div>
  <div class="abs social" style="left:546px;top:2767px"></div>
  <p class="abs center ft" style="top:2822px;font-size:9.5px">Copyright © 2019 Companyname, All Rights Reserved &nbsp;| &nbsp;Disclaimer Policy.</p>

</div>
</body>
</html>
```